Modern corporate energy/fuel business need business card design

Business card required for company founder. Korvan Halden Group is a Australian based modern energy/fuel provider. We offer specialised solutions to businesses using fossil fuels through renewable energy solutions.

I would like one side with specific information (name, address etc)

The other side to be bold, professional company name & logo. Striking.

Target Market(s)

B2B. Transport, mining, councils, environmentalist,

Industry/Entity Type

Petroleum

Contact Information for Business Card

Name; Peter Morrow
Position; Director
Email; pmorrow@korvanhalden.com.au
Address; PO Box 347, Larkvale, QLD, 4812
Website; www.korvanhalden.com.au

Colors

Designer to choose colors to be used in the design.

Requirements
Must have
• Clean, easy to read, professional & strong theme
Should not have
• too many colours, busy layout,

```html
<!DOCTYPE html>
<html lang="en">
<head>
<meta charset="utf-8">
<title>Korvan Halden Group — Business Card</title>
<link rel="stylesheet" href="https://fonts.googleapis.com/css2?family=Poppins:wght@400;500&display=swap">
<style>
  :root {
    --backdrop: #cbcbcb;
    --card-white: #ffffff;
    --card-black: #1b1c1e;
    --navy: #22507a;
    --orange: #f26a12;
    --ink: #444a50;
    --rule: #9a9a9a;
    --silver: #8d8f92;
  }
  * { box-sizing: border-box; margin: 0; padding: 0; }
  html, body {
    width: 1125px; height: 1200px; overflow: hidden;
    background: var(--backdrop);
    font-family: "Poppins", sans-serif;
  }
  .stage {
    position: relative;
    width: 1090px; height: 1163px;
    transform: scale(1.0321);
    transform-origin: 0 0;
  }
  .card {
    position: absolute;
    left: 145px; width: 800px; height: 457px;
    border-radius: 26px;
    overflow: hidden;
  }
  .card--front { top: 95px; background: var(--card-white); }
  .card--back { top: 611px; background: var(--card-black); }

  .brand {
    position: absolute;
    display: flex; align-items: center; gap: 14px;
  }
  .brand__dot { border-radius: 50%; flex: none; }
  .brand__name { font-weight: 500; white-space: nowrap; }

  .card--front .brand { right: 58px; top: 52px; }
  .card--front .brand__dot { width: 82px; height: 82px; background: var(--orange); }
  .card--front .brand__name { color: var(--navy); font-size: 30px; }

  .holder { position: absolute; left: 50px; top: 262px; }
  .holder__name { color: var(--navy); font-size: 28px; font-weight: 500; line-height: 1.1; }
  .holder__role { color: var(--orange); font-size: 18px; line-height: 1.3; }

  .divider {
    position: absolute; left: 50px; right: 59px; top: 329px;
    height: 1px; background: var(--rule);
  }
  .contacts {
    position: absolute; left: 50px; top: 346px;
    list-style: none; color: var(--ink); font-size: 18px; line-height: 26px;
  }
  .contacts li { display: flex; align-items: center; gap: 8px; }
  .contacts svg { width: 18px; height: 18px; fill: var(--navy); }
  .address {
    position: absolute; right: 58px; top: 346px;
    font-style: normal; text-align: right;
    color: var(--ink); font-size: 18px; line-height: 23px;
  }
  .footer-bands { position: absolute; left: 0; bottom: 0; width: 800px; height: 40px; }
  .website {
    position: absolute; right: 22px; bottom: 6px;
    color: #ffffff; font-size: 17px; letter-spacing: 2.6px;
  }

  .card--back .brand {
    left: 0; right: 0; top: 0; bottom: 0; justify-content: center; gap: 22px;
  }
  .card--back .brand__dot { width: 112px; height: 112px; background: var(--silver); }
  .card--back .brand__name { color: var(--silver); font-size: 40px; }
</style>
</head>
<body>
<main class="stage">

  <section class="card card--front" aria-label="Business card, front">
    <div class="brand">
      <span class="brand__dot"></span>
      <span class="brand__name">Korvan Halden Group</span>
    </div>

    <div class="holder">
      <h1 class="holder__name">Peter Morrow</h1>
      <p class="holder__role">Director</p>
    </div>

    <div class="divider"></div>

    <ul class="contacts">
      <li>
        <svg viewBox="0 0 24 24" aria-hidden="true"><path d="M6.6 10.8a15.1 15.1 0 0 0 6.6 6.6l2.2-2.2c.3-.3.7-.4 1-.2 1.1.4 2.3.6 3.6.6.6 0 1 .4 1 1V20c0 .6-.4 1-1 1A17 17 0 0 1 3 4c0-.6.4-1 1-1h3.5c.6 0 1 .4 1 1 0 1.3.2 2.5.6 3.6.1.3 0 .7-.2 1L6.6 10.8z"/></svg>
        369-481-7302
      </li>
      <li>
        <svg viewBox="0 0 24 24" aria-hidden="true"><path d="M2 5h20v14H2V5zm2 2v.4l8 5.2 8-5.2V7H4zm16 2.8-8 5.2-8-5.2V17h16V9.8z"/></svg>
        pmorrow@korvanhalden.com.au
      </li>
    </ul>

    <address class="address">PO Box 347<br>Larkvale, QLD, 4812</address>

    <svg class="footer-bands" viewBox="0 0 800 40" aria-hidden="true">
      <rect x="0" y="32" width="445" height="6" fill="var(--orange)"/>
      <polygon points="434,40 474,5 800,5 800,40" fill="var(--navy)"/>
    </svg>
    <span class="website">WWW.KORVANHALDEN.COM.AU</span>
  </section>

  <section class="card card--back" aria-label="Business card, back">
    <div class="brand">
      <span class="brand__dot"></span>
      <span class="brand__name">Korvan Halden Group</span>
    </div>
  </section>

</main>
</body>
</html>
```